Fotograf für Immobilien, Interieur und Portraits benötigt Geschäftspapiere
Zielgruppe
Fotograf für Immobilien, Interieur und Portraits.
Zielgruppe der Immobilien- und Interieur-Fotografie sind Makler, Bauträger, Wohnungsbaugesellschaften, Hotels, Eigentümer von Ferienwohnung etc.
Zielgruppe der Portraitfotografie sind Freiberufler, Selbstständige, Unternehmen und Agenturen
Aufgabenstellung
Ich wünsche mir ein modernes und dynamisches Briefpapier, das ins Auge fällt und dem Betrachter in Erinnerung bleibt. Wir wollen es für Akquise, Kundenanschreiben, Angebote und Rechnungen verwenden.
Wir verwenden bereits heute einen Orange-Ton (f29100) für unseren Webauftritt, unsere Visitenkarten etc. Gerne können Sie sich unter www.lichtwerkel.de einen Eindruck über unser Unternehmen verschaffen.
Das Briefpapier soll nachfolgende Inhalte aufweisen:
Bei Einbindung einer der hochgeladenen Vektoren bitte Firmenbezeichnung berücksichtigen.
Meine Firmenbezeichnung lichtwerkel ggfs. Zusatz Studio am Kolbweiher, die Verwendung der Farbe Orange (siehe www.lichtwerkel.de) aktueller Farbwert f29100 (bin für Farbvarianten im Farbton Orange offen!)
Name, Anschrift, USt-ID, Bankverbindung, Webadresse, Mail und Telefon
Für Rückfragen stehen wir Ihnen gerne zur Verfügung!

```html
<!DOCTYPE html>
<html lang="de">
<head>
<meta charset="utf-8">
<title>lichtwerkel – Briefpapier</title>
<link rel="stylesheet" href="https://fonts.googleapis.com/css2?family=Arimo:wght@400;700&family=Open+Sans:wght@400;600&display=swap">
<style>
  :root {
    --orange: #f29100;
    --black: #0a0a0a;
    --ink: #3a3a3a;
    --muted: #8a8a8a;
    --paper: #ffffff;
    --backdrop: #e9e9eb;
  }
  * { box-sizing: border-box; margin: 0; padding: 0; }
  html, body { width: 1200px; height: 1010px; overflow: hidden; }
  body { background: var(--backdrop); font-family: "Arimo", Arial, sans-serif; color: var(--ink); }

  .letterhead {
    position: absolute; left: 270px; top: 38px;
    width: 660px; height: 934px;
    background: var(--paper);
    box-shadow: 0 4px 18px rgba(0,0,0,.12);
    overflow: hidden;
  }
  .swoosh { position: absolute; inset: 0; width: 100%; height: 100%; }

  .brand {
    position: absolute; left: 420px; top: 118px;
    display: flex; align-items: center; gap: 8px;
    font-family: "Arimo", Arial, sans-serif; font-size: 24px; font-weight: 400;
    color: var(--black); letter-spacing: .5px;
  }
  .brand-dot { width: 14px; height: 14px; border-radius: 50%; background: var(--orange); }

  .sender-block {
    position: absolute; left: 478px; top: 168px;
    padding-left: 10px; border-left: 1px solid var(--orange);
    font-style: normal;
    font-size: 8.5px; line-height: 1.35; color: var(--black);
  }
  .sender-block .contact { display: flex; align-items: center; gap: 4px; }
  .sender-block svg { width: 7px; height: 7px; fill: var(--orange); }

  .return-line {
    position: absolute; left: 70px; top: 236px;
    font-family: "Open Sans", Arial, sans-serif; font-size: 5.5px; color: var(--black);
    border-bottom: .6px solid var(--black); padding-bottom: 1px;
  }
  .return-line .sep { color: var(--orange); }

  .fold-mark { position: absolute; left: 0; width: 16px; height: 0; border-top: .8px solid #bbb; }
  .fold-mark.upper { top: 312px; }
  .fold-mark.lower { top: 624px; }

  .letter-body {
    position: absolute; left: 112px; top: 300px; width: 430px;
    font-size: 10.5px; line-height: 1.38; color: var(--ink);
  }
  .letter-body .salutation { margin-bottom: 10px; }
  .letter-body p { margin-bottom: 12px; }

  .signature {
    position: absolute; left: 140px; top: 612px; width: 190px; height: 56px;
    background: linear-gradient(90deg, #f4f4f4, #e9e9e9);
    border-radius: 4px;
  }

  .footer {
    position: absolute; left: 150px; top: 840px;
    display: flex; gap: 12px;
    font-family: "Open Sans", Arial, sans-serif; font-size: 8px; line-height: 1.4; color: var(--black);
  }
  .footer .col + .col { border-left: 1px solid var(--orange); padding-left: 12px; }

  .web-address {
    position: absolute; left: 560px; top: 896px;
    font-family: "Open Sans", Arial, sans-serif; font-size: 8.5px; color: #fff;
    transform: rotate(-16deg); transform-origin: left center;
  }
</style>
</head>
<body>
  <main class="letterhead">
    <svg class="swoosh" viewBox="0 0 660 934" aria-hidden="true">
      <path fill="var(--black)" d="M0 0 H370 C230 18 90 46 0 72 Z"/>
      <path fill="var(--orange)" d="M0 92 C110 52 300 14 545 0 H510 C290 12 100 48 0 80 Z"/>
      <path fill="var(--black)" d="M660 934 H330 C470 918 600 885 660 838 Z"/>
      <path fill="var(--orange)" d="M660 806 C560 880 360 922 140 934 H178 C380 922 575 880 660 822 Z"/>
    </svg>

    <div class="brand"><span class="brand-dot"></span>lichtwerkel</div>

    <address class="sender-block">
      Jonas Brandt<br>
      Lindenpfad 7<br>
      64711 Talbrunn
      <div class="contact">
        <svg viewBox="0 0 10 10"><path d="M2 0.5 L4 2.5 L3 3.8 C3.8 5.4 4.8 6.4 6.2 7 L7.5 6 L9.5 8 L8 9.5 C4 9 1 6 0.5 2 Z"/></svg>
        06071 48 20 517
      </div>
      <div class="contact">
        <svg viewBox="0 0 10 10"><path d="M0 2 H10 V8 H0 Z M0 2 L5 5.5 L10 2" /></svg>
        info@lichtwerkel.de
      </div>
    </address>

    <div class="return-line">lichtwerkel <span class="sep">|</span> Lindenpfad 7 <span class="sep">|</span> 64711 Talbrunn</div>

    <span class="fold-mark upper"></span>
    <span class="fold-mark lower"></span>

    <section class="letter-body">
      <div class="salutation">Herr Wendel</div>
      <p>Lorem ipsum dolor sit amet, consectetur adipiscing elit. Proin tincidunt, lectus id malesuada cursus, lorem augue egestas magna, ut mattis orci ante ut arcu. Sed mauris tellus, fermentum quis ligula nec, posuere pulvinar eros. Nam at mi quis velit pellentesque finibus. Donec lacus velit, faucibus mollis dolor nec, finibus pellentesque orci. Duis sed dictum elit, ut posuere arcu. Phasellus ac dolor et ante consequat rutrum nec nec tortor. Donec consequat, nibh sit amet pulvinar faucibus, turpis magna venenatis diam, vel pretium eros erat vestibulum nulla.</p>
      <p>Sed pretium ac enim eu viverra. Aliquam ac est eget magna convallis convallis. Aenean augue purus, finibus eget turpis quis, finibus dignissim nibh. Phasellus viverra lobortis dignissim. Duis varius turpis in sapien accumsan facilisis. Sed vehicula gravida diam a interdum. Nullam convallis ligula id erat egestas consequat. Integer consectetur ex vel aliquet iaculis. Vestibulum molestie sodales mauris, at tincidunt risus pellentesque.</p>
      <p>Mauris facilisis, lectus at accumsan tincidunt, dui magna imperdiet sem, quis tempor est lectus eu ipsum. Praesent in fermentum nisl. Maecenas at lorem at odio interdum iaculis. Pellentesque cursus nulla nunc, ut suscipit nulla maximus et. Donec maximus rhoncus metus, vel laoreet nisi pretium sit amet. Donec posuere enim lectus, vitae aliquam augue tincidunt dignissim. Morbi vitae congue velit, quis elementum.</p>
    </section>

    <div class="signature" role="img" aria-label="Handschriftliche Unterschrift von Jonas Brandt"></div>

    <footer class="footer">
      <div class="col">lichtwerkel | Jonas Brandt<br>Umsatzsteuer ID: DE401236958</div>
      <div class="col">Bankverbindung:<br>Kreissparkasse Talbrunn</div>
      <div class="col">BIC: TALBDEF1KRS<br>IBAN: DE47 5083 1190 0034 7721 05</div>
    </footer>

    <div class="web-address">www.lichtwerkel.de</div>
  </main>
</body>
</html>
```